Commercial HVAC and Refrigeration Business cards

Frost-Haven Company is looking for flashy new business cards! We design, install, service and maintain commercial refrigeration, air conditioning, heating and refrigeration equipment. Our colors are blue and white. I'm open to single and double sided designs. Each employee will have their own business card. I've attached a copy of our current logo.

Our website, office and cell phone (cell phone is optional), email address should be clearly legible. "24 Hour Service" and the services we offer are; Sales, Service, Design, Installation, Maintenance. Refrigeration, Heating, Air Conditioning, Ice Machines. Does not have to be in any order.

Target Market(s)

Commercial; Restaurants, hotels, bars, breweries etc.

Industry/Entity Type

Hvac

Contact Information for Business Card

Name; Job Title, Phone Number, Email Address. www.frost-haven-example.com 24 Hour Service. We provide - Sales, Design, Installation, Service, Maintenance. We service - Refrigeration, Heating, Air Conditioning, Ice Machines

Font styles to use
Other font styles liked:
• Be creative

Colors
0255a3
ffffff

Requirements
Must have
• Professional appearance and appeal to commercial clients in the food-service and hospitality industry. Must be clearly legible and easy to understand.
Nice to have
• We want to sell maintenance agreements, perhaps we can use the back of the card to tie into a webpage about our maintenance agreements.
Should not have
• Cartoons or unprofessional. Nothing too edgy.

```html
<!DOCTYPE html>
<html lang="en">
<head>
<meta charset="utf-8">
<title>Frost-Haven Company – Business Cards</title>
<link rel="stylesheet" href="https://fonts.googleapis.com/css2?family=Arimo:wght@400;700&display=swap">
<style>
  :root {
    --brand-blue: #0255a3;
    --deep-blue: #0a4a94;
    --white: #ffffff;
    --muted-grey: #8a8f96;
    --stage: #e9ebee;
    --ink: #22324a;
  }
  * { box-sizing: border-box; margin: 0; padding: 0; }
  html, body { width: 1200px; height: 950px; overflow: hidden; }
  body {
    background: var(--stage);
    font-family: "Arimo", Arial, sans-serif;
    position: relative;
  }
  .card {
    position: absolute;
    width: 700px;
    height: 400px;
    border-radius: 6px;
    box-shadow: 0 10px 28px rgba(0,0,0,0.18);
    overflow: hidden;
  }
  .card-frame { position: absolute; inset: 0; width: 100%; height: 100%; }
  .card-content {
    position: absolute; inset: 0;
    display: flex; flex-direction: column; align-items: center;
  }

  /* Back of card */
  .card--back { left: 70px; top: 60px; background: var(--brand-blue); color: var(--white); }
  .card--back .brand-name {
    margin-top: 92px;
    font-size: 44px; font-weight: 700; letter-spacing: 0.5px;
    color: var(--white);
  }
  .section-title {
    margin-top: 44px;
    display: flex; align-items: center; gap: 16px;
    font-size: 21px; font-weight: 700;
  }
  .section-title::before, .section-title::after {
    content: ""; width: 120px; height: 1px; background: rgba(255,255,255,0.6);
  }
  .service-list { margin-top: 20px; font-size: 17px; line-height: 1.55; }
  .service-list dt { display: inline; font-size: 19px; }
  .service-list dd { display: inline; margin-left: 6px; }
  .service-row { white-space: nowrap; }

  /* Front of card */
  .card--front { left: 430px; top: 490px; background: var(--white); color: var(--deep-blue); }
  .card--front .brand-name {
    margin-top: 78px;
    font-size: 40px; font-weight: 700; color: var(--brand-blue);
  }
  .person {
    margin-top: 40px;
    display: flex; align-items: center; gap: 14px;
    font-size: 22px;
  }
  .person::before, .person::after {
    content: ""; width: 110px; height: 1px; background: var(--brand-blue); opacity: 0.6;
  }
  .person-name { color: var(--brand-blue); }
  .person-title { color: var(--muted-grey); }
  .contact-list { margin-top: 16px; list-style: none; text-align: center; font-size: 17px; line-height: 1.6; color: var(--ink); }
  .contact-list li { display: inline-flex; align-items: center; gap: 6px; margin: 0 8px; }
  .contact-icon { width: 16px; height: 16px; fill: var(--brand-blue); }
  .service-note { margin-top: 10px; font-size: 17px; color: var(--muted-grey); }
</style>
</head>
<body>

  <section class="card card--back" aria-label="Business card back">
    <svg class="card-frame" viewBox="0 0 700 400" aria-hidden="true">
      <path d="M44 18 H656 A26 26 0 0 0 682 44 V356 A26 26 0 0 0 656 382 H44 A26 26 0 0 0 18 356 V44 A26 26 0 0 0 44 18 Z" fill="none" stroke="#ffffff" stroke-width="2.5"/>
      <path d="M50 26 H650 A24 24 0 0 0 674 50 V350 A24 24 0 0 0 650 374 H50 A24 24 0 0 0 26 350 V50 A24 24 0 0 0 50 26 Z" fill="none" stroke="#ffffff" stroke-width="1" opacity="0.6"/>
    </svg>
    <div class="card-content">
      <div class="brand-name">Frost-Haven Company</div>
      <h2 class="section-title">Maintenance agreements</h2>
      <dl class="service-list">
        <div class="service-row"><dt>We provide :</dt><dd>Sales | Design | Installation | Service | Maintenance</dd></div>
        <div class="service-row"><dt>We service :</dt><dd>Refrigeration | Heating | Air Conditioning | Ice Machines</dd></div>
      </dl>
    </div>
  </section>

  <section class="card card--front" aria-label="Business card front">
    <svg class="card-frame" viewBox="0 0 700 400" aria-hidden="true">
      <path d="M44 18 H656 A26 26 0 0 0 682 44 V356 A26 26 0 0 0 656 382 H44 A26 26 0 0 0 18 356 V44 A26 26 0 0 0 44 18 Z" fill="none" stroke="#0255a3" stroke-width="3"/>
    </svg>
    <div class="card-content">
      <div class="brand-name">Frost-Haven Company</div>
      <p class="person"><span><span class="person-name">Sam Porter</span> <span class="person-title">- President</span></span></p>
      <ul class="contact-list">
        <li>
          <svg class="contact-icon" viewBox="0 0 24 24" aria-hidden="true"><path d="M6.6 10.8a15.1 15.1 0 0 0 6.6 6.6l2.2-2.2a1 1 0 0 1 1-.25 11.4 11.4 0 0 0 3.6.57 1 1 0 0 1 1 1V20a1 1 0 0 1-1 1A17 17 0 0 1 3 4a1 1 0 0 1 1-1h3.5a1 1 0 0 1 1 1c0 1.25.2 2.45.57 3.57a1 1 0 0 1-.25 1z"/></svg>
          555 014 2290
        </li>
        <li>
          <svg class="contact-icon" viewBox="0 0 24 24" aria-hidden="true"><path d="M3 5h18v14H3z M3 5l9 7 9-7" fill="none" stroke="#0255a3" stroke-width="2"/></svg>
          sam@frost-haven-example.com
        </li>
        <li>
          <svg class="contact-icon" viewBox="0 0 24 24" aria-hidden="true"><circle cx="12" cy="12" r="9" fill="none" stroke="#0255a3" stroke-width="2"/><path d="M3 12h18M12 3c3 3 3 15 0 18M12 3c-3 3-3 15 0 18" fill="none" stroke="#0255a3" stroke-width="1.5"/></svg>
          www.frost-haven-example.com
        </li>
      </ul>
      <p class="service-note">24 Hour Service.</p>
    </div>
  </section>

</body>
</html>
```